Silverleaf Rise Accounting Program

size of ad Full: 7” x 9.6”
1- this is for a ladies program so it should appeal to women.
2-however, I do not want any pictures of people in this ad.
3-all the text should be seen and not covered over by graphics.
4-It should be an ad that will draw people's attention and people should look at it and say it looks nice I want to see that ad.
5-I have put all the instructions in yellow in the file below.
6-please leave 1 inch for the footer .
good luck with this project

• no picture or vector of people.

```html
<!DOCTYPE html>
<html lang="en">
<head>
<meta charset="utf-8">
<title>Silverleaf Rise Accounting Program – Open House</title>
<link href="https://fonts.googleapis.com/css2?family=Yesteryear&family=Playfair+Display:wght@600;700&family=Quicksand:wght@500;600&family=Open+Sans:wght@400;800&display=swap" rel="stylesheet">
<style>
  :root {
    --bg-pink: #f9e6ee;
    --bg-lilac: #d9cdef;
    --card: #fbf8fc;
    --card-border: #6f78e2;
    --purple: #5b3592;
    --navy: #2b2482;
    --grey: #555560;
    --highlight: #fbf57a;
    --rule: #4a4aa8;
    --badge-orange: #f29a1e;
  }
  * { margin: 0; padding: 0; box-sizing: border-box; }
  html, body { width: 883px; height: 1200px; overflow: hidden; background: #ffffff; }
  .ad { position: relative; width: 883px; height: 1200px; overflow: hidden; }
  .ad-pattern {
    position: absolute; left: 15px; top: 14px; width: 855px; height: 1172px;
    background: radial-gradient(circle at 30% 30%, var(--bg-pink) 0%, #eedcec 45%, var(--bg-lilac) 100%);
  }
  .info-card {
    position: absolute; left: 140px; top: 78px; width: 610px; height: 781px;
    background: var(--card); border: 3px solid var(--card-border); border-radius: 30px;
  }
  .headline-highlight {
    position: absolute; left: 206px; top: 131px; width: 466px; height: 37px;
    background: var(--highlight); outline: 1px solid var(--highlight); outline-offset: 3px;
  }
  .headline {
    position: absolute; left: 0; width: 883px; top: 112px; text-align: center;
    font-family: "Yesteryear", cursive; font-size: 62px; line-height: 1; color: var(--purple);
  }
  .serif {
    font-family: "Playfair Display", Georgia, serif; font-weight: 700; color: var(--purple);
    letter-spacing: -0.5px; font-variant-numeric: lining-nums;
  }
  .subhead {
    position: absolute; left: 140px; width: 610px; top: 208px;
    text-align: center; font-size: 28px; line-height: 1.2;
  }
  .rule {
    position: absolute; left: 163px; width: 543px; height: 2px;
    background: linear-gradient(90deg, transparent, var(--rule) 30%, var(--rule) 70%, transparent);
  }
  .rule-top { top: 258px; }
  .rule-bottom { top: 617px; }
  .benefit { position: absolute; left: 215px; line-height: 1.15; }
  .benefit-large { font-size: 35px; }
  .benefit-small { font-size: 27px; left: 219px; }
  .tick { position: absolute; width: 18px; height: 18px; }
  .grads {
    position: absolute; left: 140px; width: 610px; top: 628px; text-align: center;
    font-family: "Quicksand", sans-serif; font-weight: 500;
    font-size: 20px; line-height: 33px; color: var(--grey);
  }
  .event {
    position: absolute; left: 140px; width: 610px; top: 695px; text-align: center;
    font-family: "Playfair Display", Georgia, serif; font-weight: 700; font-variant-numeric: lining-nums;
    font-size: 38px; line-height: 41px; color: var(--navy); letter-spacing: -0.5px;
  }
  .contact-note {
    position: absolute; left: 140px; width: 610px; top: 789px; text-align: center;
    font-family: "Quicksand", sans-serif; font-weight: 500; font-size: 15px; color: #222;
  }
  .contact-details {
    position: absolute; left: 140px; width: 610px; top: 811px; text-align: center;
    font-family: "Quicksand", sans-serif; font-weight: 600; font-size: 18px; color: var(--purple);
  }
  .ranking-box {
    position: absolute; left: 142px; top: 872px; width: 315px; height: 171px;
    background: rgba(255,255,255,0.85); border-radius: 14px;
  }
  .ranking-badge {
    position: absolute; left: 170px; top: 900px; width: 96px; height: 96px; border-radius: 50%;
    background: radial-gradient(circle, #f9c23c 0%, var(--badge-orange) 100%);
  }
  .ranking-divider {
    position: absolute; left: 288px; top: 882px; width: 2px; height: 152px; background: var(--navy);
  }
  .ranking-text {
    position: absolute; left: 303px; top: 884px; width: 152px;
    font-family: "Open Sans", sans-serif; font-weight: 400;
    font-size: 15.5px; line-height: 20.4px; color: #111; white-space: nowrap;
  }
  .starburst {
    position: absolute; left: 512px; top: 852px; width: 236px; height: 236px;
    filter: drop-shadow(4px 6px 5px rgba(80,60,120,0.35));
  }
  .starburst-label {
    position: absolute; left: 512px; top: 920px; width: 236px; text-align: center;
    font-family: "Open Sans", sans-serif; font-weight: 800;
    font-size: 30px; line-height: 30px; color: var(--purple);
  }
</style>
</head>
<body>
<main class="ad">
  <div class="ad-pattern" role="img" aria-label="Decorative lavender floral swirl pattern on soft pink background"></div>

  <section class="info-card"></section>

  <div class="headline-highlight"></div>
  <h1 class="headline">Attention Women:</h1>

  <h2 class="subhead serif">The Silverleaf Rise Job Placement advantage</h2>
  <div class="rule rule-top"></div>

  <svg class="tick" style="left:188px;top:276px" viewBox="0 0 20 20"><circle cx="10" cy="10" r="8.5" fill="none" stroke="#5b3592" stroke-width="1.6"/><path d="M6 10.3l2.7 2.7L14.2 7.4" fill="none" stroke="#5b3592" stroke-width="1.8"/></svg>
  <p class="benefit benefit-large serif" style="top:264px">96% Placement Rate -</p>

  <svg class="tick" style="left:188px;top:327px" viewBox="0 0 20 20"><circle cx="10" cy="10" r="8.5" fill="none" stroke="#5b3592" stroke-width="1.6"/><path d="M6 10.3l2.7 2.7L14.2 7.4" fill="none" stroke="#5b3592" stroke-width="1.8"/></svg>
  <p class="benefit benefit-large serif" style="top:309px">6 placement directors -</p>

  <svg class="tick" style="left:188px;top:366px" viewBox="0 0 20 20"><circle cx="10" cy="10" r="8.5" fill="none" stroke="#5b3592" stroke-width="1.6"/><path d="M6 10.3l2.7 2.7L14.2 7.4" fill="none" stroke="#5b3592" stroke-width="1.8"/></svg>
  <p class="benefit benefit-large serif" style="top:354px">Decades of relationships with<br>100’s of firms</p>

  <svg class="tick" style="left:193px;top:468px" viewBox="0 0 20 20"><circle cx="10" cy="10" r="8.5" fill="none" stroke="#5b3592" stroke-width="1.6"/><path d="M6 10.3l2.7 2.7L14.2 7.4" fill="none" stroke="#5b3592" stroke-width="1.8"/></svg>
  <p class="benefit benefit-small serif" style="top:457px">A Master’s Degree in Accounting</p>

  <svg class="tick" style="left:193px;top:509px" viewBox="0 0 20 20"><circle cx="10" cy="10" r="8.5" fill="none" stroke="#5b3592" stroke-width="1.6"/><path d="M6 10.3l2.7 2.7L14.2 7.4" fill="none" stroke="#5b3592" stroke-width="1.8"/></svg>
  <p class="benefit benefit-small serif" style="top:497px;line-height:37px">A stable, lucrative career, with high-<br>paying, full / part time opportunities in<br>Private/Public companies</p>

  <div class="rule rule-bottom"></div>

  <p class="grads">Graduates have been placed in top companies<br>(full/part time jobs).</p>

  <p class="event">Meetwave open house<br>Sunday June 14, 2.00pm</p>

  <p class="contact-note">for a Meetwave link / conference number /information</p>
  <p class="contact-details">info@silverleafrise.org &nbsp;or 555 014 2280 x 111</p>

  <div class="ranking-box"></div>
  <div class="ranking-badge" role="img" aria-label="Program ranking award badge"></div>
  <div class="ranking-divider"></div>
  <p class="ranking-text">Halbrook Vale<br>University,<br>Masters in<br>Accounting program,<br>received the highest<br>possible rating<br>in USA</p>

  <svg class="starburst" viewBox="-118 -118 236 236" aria-hidden="true">
    <polygon transform="rotate(15) scale(1.06)" fill="none" stroke="#5b3592" stroke-width="1.5"
      points="108,0 77.3,20.7 93.5,54 56.6,56.6 54,93.5 20.7,77.3 0,108 -20.7,77.3 -54,93.5 -56.6,56.6 -93.5,54 -77.3,20.7 -108,0 -77.3,-20.7 -93.5,-54 -56.6,-56.6 -54,-93.5 -20.7,-77.3 0,-108 20.7,-77.3 54,-93.5 56.6,-56.6 93.5,-54 77.3,-20.7"/>
    <polygon fill="#fbf57a"
      points="108,0 77.3,20.7 93.5,54 56.6,56.6 54,93.5 20.7,77.3 0,108 -20.7,77.3 -54,93.5 -56.6,56.6 -93.5,54 -77.3,20.7 -108,0 -77.3,-20.7 -93.5,-54 -56.6,-56.6 -54,-93.5 -20.7,-77.3 0,-108 20.7,-77.3 54,-93.5 56.6,-56.6 93.5,-54 77.3,-20.7"/>
  </svg>
  <p class="starburst-label">MASTERS<br>in<br>12 months</p>
</main>
</body>
</html>
```